Velmora Commercial Finance Information Brochure

This brochure will be sent out to clients via A4 PDF on an email to showcase what our company has to offer. We are a commercial finance brokerage, that specialises in property finance. We would like to see designs following our colour scheme. The final design should demonstrate our professionalism and reliability.
I have attached our logo and also a few bullet points on our information and what we can offer. These can be slightly reworded for conciseness. Or leave the text sections as filler and I can fill these in.
I have also attached an overview of our colour scheme and design styling for your consideration.
Target Market(s)
Property Developers
Industry/Entity Type
Financial Services
Look and feel
Each slider illustrates characteristics of the customer's brand and the style your logo design should communicate.

```html
<!DOCTYPE html>
<html lang="en">
<head>
<meta charset="utf-8">
<title>Velmora Finance – Information Brochure</title>
<link href="https://fonts.googleapis.com/css2?family=Montserrat:wght@700;800&family=Quicksand:wght@500;600;700&display=swap" rel="stylesheet">
<style>
  :root {
    --bg: #e9e9ec;
    --paper: #ffffff;
    --brand-blue: #1740a8;
    --brand-green: #1f8a3f;
    --deep-blue: #0e45b5;
    --ink: #2c2c34;
    --white: #ffffff;
    --sky: #8fb3d9;
    --sand: #c9b89a;
  }
  * { margin: 0; padding: 0; box-sizing: border-box; }
  html, body { width: 1200px; height: 800px; overflow: hidden; background: var(--bg); }
  .brochure {
    position: absolute; left: 332px; top: 21px;
    width: 536px; height: 758px;
    background: var(--paper);
    box-shadow: 0 4px 18px rgba(0,0,0,.15);
    font-family: "Quicksand", sans-serif;
    color: var(--ink);
    overflow: hidden;
  }
  .brand-name {
    position: absolute; left: 44px; top: 52px;
    font-family: "Quicksand", sans-serif;
    font-weight: 700; font-size: 26px; letter-spacing: 1px;
    color: var(--brand-blue);
    display: flex; align-items: center; gap: 8px;
    text-transform: uppercase;
  }
  .brand-mark { width: 14px; height: 14px; background: var(--brand-green); }
  .hero-photo {
    position: absolute; left: 28px; right: 0; top: 100px; height: 300px;
    background: linear-gradient(180deg, var(--sky) 0%, #b9cde0 45%, var(--sand) 78%, #a89a85 100%);
  }
  .about-panel {
    position: absolute; left: 44px; top: 372px; width: 244px; height: 332px;
    background: linear-gradient(180deg, var(--brand-green) 0%, #16707a 50%, var(--deep-blue) 100%);
    border-radius: 0 0 8px 8px;
    padding: 16px 16px;
    color: var(--white);
  }
  .about-panel h2 {
    font-family: "Montserrat", sans-serif; font-weight: 800;
    font-size: 12.5px; line-height: 1.25; margin-bottom: 10px;
  }
  .about-panel p, .details p {
    font-size: 7.2px; line-height: 1.48; font-weight: 500;
    text-align: justify; margin-bottom: 10px;
  }
  .details {
    position: absolute; left: 310px; top: 414px; width: 196px;
  }
  .details p { margin-bottom: 11px; }
  .contact-band {
    position: absolute; left: 0; right: 0; bottom: 0; height: 40px;
    background: linear-gradient(90deg, var(--deep-blue) 0%, #167a6a 55%, var(--brand-green) 100%);
    display: flex; align-items: center; justify-content: space-around;
    padding: 0 14px;
    color: var(--white); font-weight: 700; font-size: 10.5px;
  }
  .contact-item { display: flex; align-items: center; gap: 6px; }
  .contact-item svg { width: 13px; height: 13px; }
</style>
</head>
<body>
<main class="brochure">
  <div class="brand-name"><span class="brand-mark"></span>Velmora Finance</div>

  <div class="hero-photo" role="img" aria-label="Photo of construction workers in hi-vis vests and hard hats walking towards a steel-frame building site with a crane"></div>

  <section class="about-panel">
    <h2>What sets us apart?<br>Well, we’ve walked in your shoes.</h2>
    <p>As former lenders and developers ourselves, we intimately understand the inefficiencies that plague deals in the market today. We’ve experienced the frustration of tight time limits on deals and the exasperating feeling of brokers wasting precious time collecting information. It’s enough to drive developers &amp; lenders insane!</p>
    <p>That’s why we founded Velmora Finance – to be the efficient &amp; reliable link that connects developers and lenders. We’ve streamlined our processes to eliminate unnecessary hurdles, enabling clear and swift communication between all parties involved. No more wasted time. No more unnecessary stress.</p>
    <p>With our expertise and industry insights, we’ve developed a unique approach that simplifies the financing journey. From the initial consultation to the final funding, we’re here to guide you every step of the way. Our goal? To make commercial financing a smooth and enjoyable experience for you.</p>
  </section>

  <section class="details">
    <p>With our background in the asset management industry, we have cultivated a black book of fund managers, institutions, UHNWI and private equity lenders that we can call on for non-traditional lending.</p>
    <p>Velmora Finance was created to satisfy a need in the market that has been far too overlooked. Efficiency. Efficiency is at the heart of our operations, &amp; we pride ourselves on our ability to secure the best financing options swiftly and effectively for our clients. By employing cutting-edge technology and streamlining our internal processes, we have cultivated a seamless and time-saving approach to finance brokering. Having been a developer, we understand the stresses and headaches associated with building, let alone all the paperwork and emails backwards &amp; forwards between yourself and brokers to attain the necessary financing.</p>
    <p>We are well-versed in the questions lenders will ask, allowing us to get ahead of the curve and request all the necessary information from you on day one. This approach provides you with a distinct advantage, as it eliminates the need to allocate hours each day to answering questions &amp; fulfilling requests from brokers. By entrusting us with this responsibility, you can focus on your core tasks and leave the financing aspect to us, making the process less stressful for you.</p>
  </section>

  <footer class="contact-band">
    <div class="contact-item">
      <svg viewBox="0 0 16 16" aria-hidden="true"><circle cx="8" cy="8" r="7" fill="none" stroke="#fff" stroke-width="1.2"/><path d="M5.5 4.5l1.4 1.6-.8 1.1c.5 1 1.3 1.8 2.3 2.3l1.1-.8 1.6 1.4-.9 1.2C7.6 11 5 8.4 4.7 5.4z" fill="#fff"/></svg>
      <span>0800 555 0142</span>
    </div>
    <div class="contact-item">
      <svg viewBox="0 0 16 16" aria-hidden="true"><circle cx="8" cy="8" r="7" fill="none" stroke="#fff" stroke-width="1.2"/><rect x="4" y="5.3" width="8" height="5.4" fill="none" stroke="#fff" stroke-width="1"/><path d="M4 5.5l4 3 4-3" fill="none" stroke="#fff" stroke-width="1"/></svg>
      <span>enquiries@velmorafinance.co.uk</span>
    </div>
    <div class="contact-item">
      <svg viewBox="0 0 16 16" aria-hidden="true"><circle cx="8" cy="8" r="7" fill="none" stroke="#fff" stroke-width="1.2"/><circle cx="8" cy="8" r="4" fill="none" stroke="#fff" stroke-width="0.9"/><path d="M4 8h8M8 4c-1.5 1.2-1.5 6.8 0 8M8 4c1.5 1.2 1.5 6.8 0 8" fill="none" stroke="#fff" stroke-width="0.8"/></svg>
      <span>www.velmorafinance.co.uk</span>
    </div>
  </footer>
</main>
</body>
</html>
```